KEV.PRO- Darren Holcombe Fitness- needs a clever business card using the logo, name, info, contact

I need a business card designed for my Online Personal Training company called KEV.PRO, abbreviation for Darren Holcombe Fitness. My company focuses on coaching in personal health and personal growth to unleash your greatest potential. I would like to see designs that use my color scheme of a redish-orange (C:0,M:84,Y:100,K:0), grey, white, black, and my company font is OSWALD. The final design should communicate some aspects of design, health, motivation, growth, in some way. The logo is very important to the company and can be displayed in any of the colors previously mentioned. Must include the company name, my website: www.kev-pro.example , my email: dan@kev-pro.example

Target Market(s)

Personal health, fitness, general public, those who lack knowledge, awareness, and confidence in personal health

Industry/Entity Type

Personal Trainer

Font styles to use
Other font styles liked:
• OSWALD. (Bold, Regular, Light)

Colors
f37122
ffffff
9d9d9d
000000

Requirements
Must have
• Must include the logo, company name, my website: www.kev-pro.example , my email: dan@kev-pro.example
Nice to have
• Variations of the colors scheme of a redish-orange (C:0,M:84,Y:100,K:0), grey, white, black. Logo, card, or text can be in any of these colors.
• Possible quote like "Take control of your personal health to unleash your greatest potential" or "Unleashing your greatness first begins with fitness of the body and mind"

```html
<!DOCTYPE html>
<html lang="en">
<head>
<meta charset="utf-8">
<title>KEV.PRO Business Card</title>
<link rel="stylesheet" href="https://fonts.googleapis.com/css2?family=Oswald:wght@300;400;500;700&display=swap">
<style>
  :root {
    --orange: #f37122;
    --orange-deep: #e8591f;
    --white: #ffffff;
    --paper: #f7f7f7;
    --grey: #9d9d9d;
    --grey-light: #d9d9d9;
    --black: #1e1e1e;
    --backdrop: #2b2b2b;
  }
  html, body {
    margin: 0;
    padding: 0;
    width: 1200px;
    height: 1200px;
    overflow: hidden;
    background: var(--backdrop);
    font-family: "Oswald", "Arial Narrow", sans-serif;
  }
  .canvas {
    position: relative;
    width: 1200px;
    height: 1200px;
  }
  .card {
    position: absolute;
    top: 156px;
    width: 527px;
    height: 920px;
    background: var(--paper);
    overflow: hidden;
  }
  .card--front { left: 67px; }
  .card--back { left: 608px; }

  /* Front */
  .watermark-name {
    position: absolute;
    left: 0;
    top: 0;
  }
  .brand-mark {
    position: absolute;
    display: flex;
    align-items: center;
    gap: 14px;
    color: var(--orange-deep);
    font-weight: 700;
    line-height: 1;
  }
  .brand-mark__dot {
    border-radius: 50%;
    background: var(--orange-deep);
    flex: none;
  }
  .card--front .brand-mark {
    left: 40px;
    top: 276px;
    font-size: 84px;
  }
  .card--front .brand-mark__dot { width: 40px; height: 40px; }
  .front-name {
    position: absolute;
    left: 30px;
    top: 628px;
    margin: 0;
    font-size: 40px;
    font-weight: 500;
    letter-spacing: 0.3px;
    color: var(--black);
    text-transform: uppercase;
    white-space: nowrap;
  }
  .front-web {
    position: absolute;
    left: 31px;
    top: 687px;
    margin: 0;
    font-size: 26px;
    font-weight: 400;
    color: var(--orange);
  }

  /* Back */
  .pose-icon {
    position: absolute;
    left: 62px;
    top: 30px;
    width: 50px;
    height: 50px;
    background: var(--orange);
    border-radius: 4px;
  }
  .contact-list {
    position: absolute;
    left: 28px;
    top: 88px;
    margin: 0;
    padding: 0;
    list-style: none;
  }
  .contact-list li {
    display: flex;
    align-items: center;
    gap: 10px;
    font-size: 28px;
    line-height: 30px;
    color: var(--black);
  }
  .contact-list svg { width: 16px; height: 16px; flex: none; }
  .card--back .brand-mark {
    left: 0;
    width: 527px;
    justify-content: center;
    top: 318px;
    font-size: 60px;
  }
  .card--back .brand-mark__dot { width: 28px; height: 28px; }
  .back-title {
    position: absolute;
    left: 0;
    width: 527px;
    top: 490px;
    text-align: center;
    line-height: 1;
  }
  .back-title__name {
    display: block;
    font-size: 42px;
    font-weight: 700;
    color: var(--black);
  }
  .back-title__sub {
    display: block;
    margin-top: 2px;
    font-size: 12px;
    font-weight: 400;
    color: var(--black);
    text-transform: uppercase;
  }
  .service-band {
    position: absolute;
    left: 0;
    bottom: 0;
    width: 527px;
    height: 363px;
    background: var(--orange);
  }
  .service-band__text {
    position: absolute;
    left: 55px;
    top: 120px;
    margin: 0;
    color: var(--white);
    text-transform: uppercase;
    line-height: 1;
  }
  .service-band__text span { display: block; }
  .service-line--light { font-size: 34px; font-weight: 300; }
  .service-line--regular { font-size: 50px; font-weight: 400; margin-top: 14px; }
  .service-line--bold { font-size: 70px; font-weight: 700; margin-top: 6px; }
</style>
</head>
<body>
<main class="canvas">

  <section class="card card--front" aria-label="Card front">
    <svg class="watermark-name" width="527" height="920" viewBox="0 0 527 920" aria-hidden="true">
      <text x="-676" y="520" transform="rotate(-90)" textLength="622" lengthAdjust="spacingAndGlyphs"
            font-family="Oswald, sans-serif" font-weight="700" font-size="200" fill="#e2e2e2">KEV.PRO</text>
    </svg>
    <div class="brand-mark">
      <span class="brand-mark__dot"></span>
      <span class="brand-mark__name">KEV.PRO</span>
    </div>
    <h1 class="front-name">Darren Holcombe Fitness</h1>
    <p class="front-web">www.kev-pro.example</p>
  </section>

  <section class="card card--back" aria-label="Card back">
    <div class="pose-icon" role="img" aria-label="Small orange pictogram of a person in a fitness pose"></div>
    <ul class="contact-list">
      <li>
        <svg viewBox="0 0 16 16" aria-hidden="true"><rect x="1" y="3" width="14" height="10" fill="var(--orange)"/><path d="M1 3 L8 9 L15 3" fill="none" stroke="#fff" stroke-width="1.4"/></svg>
        dan@kev-pro.example
      </li>
      <li>
        <svg viewBox="0 0 16 16" aria-hidden="true"><g fill="none" stroke="var(--orange)" stroke-width="1.3"><circle cx="8" cy="8" r="6.5"/><ellipse cx="8" cy="8" rx="3" ry="6.5"/><line x1="1.5" y1="8" x2="14.5" y2="8"/></g></svg>
        www.kev-pro.example
      </li>
    </ul>
    <div class="brand-mark">
      <span class="brand-mark__dot"></span>
      <span class="brand-mark__name">KEV.PRO</span>
    </div>
    <div class="back-title">
      <span class="back-title__name">KEV.PRO</span>
      <span class="back-title__sub">Darren Holcombe.Fitness</span>
    </div>
    <div class="service-band">
      <p class="service-band__text">
        <span class="service-line--light">Online</span>
        <span class="service-line--regular">Personal</span>
        <span class="service-line--bold">Training</span>
      </p>
    </div>
  </section>

</main>
</body>
</html>
```